Booklet for meditation CD to match existing CD cover

We need a design for a booklet that matches the meditation CD cover previously designed. It should look like it belongs to the CD as it will be inserted into the cover slot. I hope you can re-use some of the existing artwork. It should incorporate the logo and the text and probably the list of tracks as well. I have attached the original CD cover file, the logo file, photo file and the specs from the CD production company for the 8 page booklet. The spec also includes a cover spec. You can ignore that part. Please put all the text from the CD cover, as well as the track names and the credits from the CD cover into the booklet and the text describing the meditation in full which I have enclosed as a word file.

Target Market(s)

People interested in meditation and personal growth

Font styles to use
Serif

Colors
0555a3
876aae
a54499
e667a6
ee363c

Requirements
Must have
• must match the existing CD cover, must include logo and photo and text from CD cover
• Design, Fonts and colours should match CD cover.

```html
<!DOCTYPE html>
<html lang="en">
<head>
<meta charset="utf-8">
<title>Meditation Booklet – Inner Spread</title>
<link href="https://fonts.googleapis.com/css2?family=Cinzel:wght@400;500&family=Roboto+Condensed:wght@500&display=swap" rel="stylesheet">
<style>
  :root {
    --sky-top: #a99dcf;
    --sky-mid: #d8b8d6;
    --sky-glow: #ecc0cd;
    --sky-low: #d58fb4;
    --sky-base: #b978a8;
    --ink: #1d1224;
    --chakra-head: #a8326f;
    --stage-head: #4d1b7d;
  }
  * { margin: 0; padding: 0; box-sizing: border-box; }
  html, body { width: 1200px; height: 595px; overflow: hidden; background: #fff; }
  .spread { position: relative; width: 1200px; height: 595px; display: flex; }
  .page {
    position: relative; width: 600px; height: 595px; overflow: hidden;
  }
  .page-backdrop {
    position: absolute; inset: 0;
    background:
      radial-gradient(ellipse 70% 40% at 50% 55%, rgba(240,200,210,.55), transparent 70%),
      linear-gradient(180deg, var(--sky-top) 0%, var(--sky-mid) 32%, var(--sky-glow) 55%, var(--sky-low) 80%, var(--sky-base) 100%);
  }
  .page--left .page-backdrop { background-position: left; }
  .page--right .page-backdrop { filter: brightness(1.03); }
  .block {
    position: absolute;
    font-family: "Roboto Condensed", "Arial Narrow", sans-serif;
    font-weight: 500;
    font-size: 12.2px;
    line-height: 16.9px;
    color: var(--ink);
  }
  .page--left .block { left: 28px; width: 546px; }
  .page--right .block { left: 28px; width: 542px; }
  .chakra-title {
    position: absolute; left: 28px;
    font-family: "Cinzel", Georgia, serif;
    font-style: italic;
    font-size: 14.5px;
    color: var(--chakra-head);
    letter-spacing: .3px;
  }
  .stage-title {
    font-family: "Cinzel", Georgia, serif;
    font-weight: 500;
    font-size: 19px;
    line-height: 19px;
    color: var(--stage-head);
    letter-spacing: .6px;
  }
  .stage-inline { font-size: 17.5px; }
  .stage-heading {
    position: absolute; left: 28px; width: 560px;
  }
</style>
</head>
<body>
<main class="spread">
  <section class="page page--left">
    <div class="page-backdrop" role="img" aria-label="Soft violet and pink dusk sky over distant mountains with a faint mandala ornament"></div>

    <h3 class="chakra-title" style="top:23px">6th Chakra: Third Eye – Intuition</h3>
    <p class="block" style="top:45px">And then let that energy of a yes to your being flow up into the centre of intuition, the point between your eyebrows. It’s the gateway beyond your physical self, sometimes felt as a deep inner knowing or being in touch with divine wisdom. The more you pay attention to this point, entering into a deep listening, the more you will receive. Don’t worry if you don’t feel anything at first. It’s a practice and it may be a sense that you haven’t used in a while. Enter with curiosity into the possibility.</p>

    <h3 class="chakra-title" style="top:157px">7th Chakra: Crown</h3>
    <p class="block" style="top:179px">Whatever you find, you let that energy also move upwards to the crown of your head or just above it. Allow your attention to expand out beyond yourself, allowing that connection with spirit that at some level you have known since the beginning of time. You may have had glimpses of this ground of consciousness that is beyond the physical realm. Allow yourself to be still, melting into this ethereal state just as a drop of rain dissolves into the ocean. Enter One-ness. No doing, no trying. Simply being with whatever arises as you allow your consciousness to expand.</p>

    <p class="block" style="top:308px"><span class="stage-title stage-inline">Fifth Stage:</span> Receiving the energy of the infinite and standing in that consciousness and giving yourself the delicious gift of complete stillness without any movement for two minutes.</p>

    <h2 class="stage-title stage-heading" style="top:369px">Sixth Stage: You are guided back, grounding all this energy down into your physical body.</h2>
    <p class="block" style="top:412px">Your body still alive from the earlier stages of your journey and still open to receive and be enriched by the Source of existence. Allow that flow of energy to enrich and enlighten your physical body, opening each centre in turn: your third eye, your throat, your heart, your power centre, your sex and your root chakra. Allow this flow of Spirit back into your being and into the earth beneath your feet, feeling yourself one part of the infinite flow of existence. And feel the flow of your nature rising up to meet Spirit in one eternal, never ending cycle. Stay alive to all that is moving in you and find your way into sitting in stillness.</p>
    <p class="block" style="top:541px">Sitting in meditation for 15 minutes.</p>
  </section>

  <section class="page page--right">
    <div class="page-backdrop" role="img" aria-label="Soft pink and lilac sky over misty mountains with a large faint mandala ornament"></div>

    <p class="block" style="top:29px">A word about sitting. To get the most out of any silent sitting meditation, it is recommended that you keep your spine upright as if there were an invisible thread from the crown of your head pulling upwards while your body remains relaxed. It is more important to be comfortable than to contort your body or force it into a position that doesn’t let you relax. Ideally you will have three points making contact with the floor. If you know how to sit in the lotus position and can relax there, that’s wonderful. If you can sit cross-legged supported by a cushion with both knees touching the floor, that works well. If you are balancing on your sit bones with nothing else to support you, you’re probably going to end slumping. In that case, it is usually better to either sit against a wall or sit in a chair or stand. With an upright spine you are holding yourself between total relaxation and total attention so that you could spring up like a samurai warrior.</p>
    <p class="block" style="top:223px">As you sit silently listening to all the life that flows within you, you may find it helpful to keep your attention on your breath. In any case, any time you find yourself lost in some thought, simply let go and bring yourself back to this present moment.</p>

    <h2 class="stage-title stage-heading" style="top:284px;width:540px">Seventh Stage: Celebration and Returning to Your Day</h2>
    <p class="block" style="top:327px">Finally, as the music brings you back to end your meditation, allow it to call you into the beauty of this moment, into a celebration of life and all that it gives you, and especially into a celebration of this wholeness, this totality of being that you are, here, now today. Take this out into your day.</p>
  </section>
</main>
</body>
</html>
```